The Maple Sprout Clinic needs a Letterhead

We are a bilingual pediatric clinic located in Montreal, Canada.

Our english name is Maple Sprout Clinic
Our french name is Clinique du petit ruisseau

We offer complete care for children including general pediatric care, pediatric specialist care such as Ear, Nose and Throat, Urology, Neurology and Adolescent Medicine. We also have paramedical specialists such as psychologists, social workers, occupational therapists, speech and language pathologists.

The letterhead must use and be harmonious with our new logo. See Design #4923293. We need two types of letterhead. One for a the Logo and both english and french names on the top and the second with the list of current staff on the left. I have uploaded two old examples for you to see. Thanks and good luck.

Font styles to use
Sans Serif

Colors
3176b5
9d9d9d

Requirements
Must have
• Include our logo.
Nice to have
• Most of our printing is done in black and white. So a grayscale design is fine.
I have included a color and grayscale versions of our logo.

We prefer clean modern designs.

```html
<!DOCTYPE html>
<html lang="en">
<head>
<meta charset="utf-8">
<title>Maple Sprout Clinic — Letterhead</title>
<link href="https://fonts.googleapis.com/css2?family=Questrial&family=Courier+Prime&display=swap" rel="stylesheet">
<style>
  :root {
    --backdrop: #e4e4e4;
    --paper: #ffffff;
    --brand-grey: #9d9d9d;
    --ink: #4f4f4f;
  }
  html, body {
    margin: 0;
    padding: 0;
    width: 1200px;
    height: 1105px;
    overflow: hidden;
    background: var(--backdrop);
  }
  .letterhead {
    position: absolute;
    left: 246px;
    top: 94px;
    width: 707px;
    height: 917px;
    background: var(--paper);
  }
  .masthead {
    position: absolute;
    top: 38px;
    left: 0;
    width: 100%;
    display: flex;
    justify-content: center;
    align-items: center;
    gap: 12px;
    font-family: "Questrial", sans-serif;
    font-size: 16px;
    line-height: 20px;
    color: var(--brand-grey);
  }
  .masthead__name {
    width: 150px;
  }
  .masthead__name--fr { text-align: right; }
  .masthead__name--en { text-align: left; }
  .masthead__dot {
    width: 44px;
    height: 44px;
    border-radius: 50%;
    background: var(--brand-grey);
    flex: none;
  }
  .contact {
    position: absolute;
    top: 842px;
    left: 0;
    width: 100%;
    text-align: center;
    font-family: "Courier Prime", monospace;
    font-size: 16px;
    line-height: 17px;
    color: var(--ink);
  }
  .contact p { margin: 0; }
</style>
</head>
<body>
  <main class="letterhead">
    <header class="masthead">
      <div class="masthead__name masthead__name--fr">Clinique<br>du petit<br>ruisseau</div>
      <span class="masthead__dot" aria-hidden="true"></span>
      <div class="masthead__name masthead__name--en">Maple<br>Sprout<br>Clinic</div>
    </header>
    <footer class="contact">
      <p class="contact__address">2210 boul. des Érables, Suite 100, Montréal, Qc, H4X 1B2</p>
      <p class="contact__phones">tel (514) 555-0142 fax (514) 555-0178</p>
    </footer>
  </main>
</body>
</html>
```